Clara Joy Halden- Lantern Waltz- Autumn/Winter Tour Dates

I need high res A3 Tour poster for print and for social media JPG sharing of tour dates.
Also needed Facebook/Twitter Banner Cover Photos of these dates.
Text Needed Below
Clara Joy Halden
Lantern Waltz
Autumn/Winter Tour Dates
03/09 Ravensby Folk Festival
21/09 Swindon- Calder Theatre
01/10 Hitchin- Brackwell Folk Club
17/10 Bath- The Anvil
20/10 Sheffield- Upper Dale Croquet Club
24/10 Birmingham- Orchard Lamp Cafe
26/10 Glasgow- The Nook and Jar
27/10 Edinburgh - The Marble Parlour
08/11 Capital Reel and Ballad Festival- The Crooked Heron
25/11 Lewes- Tandem Record Shop- Live In Store
02/12 Cambridge- The Quayside
27/01 Lincolnshire- Fenmarsh Theatre
Tickets/Info: www.clarajoyhalden-music.example/gigs
(Quotes/Reviews To Put On)
"Outstanding, rich and expressive."            "Vibrant and Experimental"
**** BdM                                                               **** Tunepaths
"Impressive and Invigorating"                        "Enchanting" Acoustic Wire UK
tBarks

Updates
I cannot read the tour dates on most of the submissions so far. They need to be visible to viewers.
Thank You.
Please also be as creative and inventive as possible- not bland.

Target Market(s)
Music Fans- Folk Acoustic Americana
Industry/Entity Type
Media
Font styles to use
Requirements
Must have
- My photo featured prominently
- Look classy and not tacky or OTT
- Look elegant, wintery and eye catching
- The dates must be very clear to read
- Links to Website:

Nice to have
- Something innovative and not boring in terms of layout design
- Perhaps fading/ misty or wintery

Should not have
- Any colours that do not match

```html
<!DOCTYPE html>
<html lang="en">
<head>
<meta charset="utf-8">
<title>Clara Joy Halden – Lantern Waltz Tour Poster</title>
<link rel="stylesheet" href="https://fonts.googleapis.com/css2?family=Allura&family=Crimson+Pro:ital,wght@0,400;1,400&display=swap">
<style>
  :root {
    --page: #ffffff;
    --ink-black: #060608;
    --photo-deep: #141620;
    --photo-mid: #3a3f4e;
    --photo-light: #6b7080;
    --text-white: #f4f4f6;
    --accent-blue: #6fa3c0;
    --frame-line: #d9d9de;
  }
  * { margin: 0; padding: 0; box-sizing: border-box; }
  html, body {
    width: 1200px; height: 1000px; overflow: hidden;
    background: var(--page);
  }
  .poster {
    position: absolute; left: 266px; top: 29px;
    width: 667px; height: 942px;
    background: var(--ink-black);
    overflow: hidden;
    font-family: "Crimson Pro", Georgia, serif;
    color: var(--text-white);
  }
  .poster h1, .poster h2 { font-weight: 400; }
  .poster__photo {
    position: absolute; left: 0; top: 0; width: 667px; height: 720px;
    background:
      radial-gradient(ellipse 170px 230px at 335px 300px, rgba(170,170,190,0.35), transparent 75%),
      radial-gradient(ellipse 260px 340px at 340px 320px, rgba(20,24,40,0.9), transparent 80%),
      radial-gradient(ellipse 400px 300px at 560px 180px, var(--photo-light), transparent 70%),
      radial-gradient(ellipse 380px 300px at 90px 260px, var(--photo-mid), transparent 75%),
      linear-gradient(180deg, var(--photo-mid) 0%, var(--photo-deep) 55%, var(--ink-black) 100%);
  }
  .quote { position: absolute; top: 40px; font-style: italic; font-size: 22px; line-height: 25px; letter-spacing: 3px; }
  .quote--left { left: 34px; }
  .quote--right { right: 38px; text-align: right; }
  .quote__source {
    display: block; margin-top: 10px;
    font-style: normal; font-size: 11px; letter-spacing: 2px;
    text-transform: uppercase; color: var(--accent-blue);
  }
  .quote--right .quote__source { font-style: italic; }
  .frame { position: absolute; left: 0; top: 0; }
  .artist-name {
    position: absolute; left: 0; width: 667px; top: 428px;
    text-align: center; font-family: "Allura", cursive;
    font-size: 82px; line-height: 90px;
  }
  .album-title {
    position: absolute; left: 0; width: 667px; top: 522px; padding-left: 100px;
    text-align: center;
    font-size: 18px; line-height: 24px; letter-spacing: 12px; text-transform: uppercase; white-space: nowrap;
  }
  .tour-heading {
    position: absolute; left: 0; width: 667px; top: 574px;
    text-align: center; font-style: italic; font-size: 23px; line-height: 30px; letter-spacing: 3px;
  }
  .dates {
    position: absolute; left: 0; width: 667px; top: 626px;
    list-style: none; text-align: center;
  }
  .dates li {
    font-size: 15px; line-height: 19px; height: 19px; letter-spacing: 2px; white-space: nowrap;
  }
  .dates .date { color: var(--accent-blue); font-style: italic; }
  .dates .date sup {
    font-size: 8px; line-height: 0; vertical-align: 0;
    position: relative; top: -0.8em;
  }
  .dates .city { text-transform: uppercase; }
  .dates .venue { font-style: italic; }
  .tickets {
    position: absolute; left: 0; width: 667px; top: 896px;
    text-align: center; font-size: 19px; line-height: 24px; letter-spacing: 2px; white-space: nowrap;
  }
  .tickets__label { color: var(--accent-blue); text-transform: uppercase; }
  .tickets__url { font-style: italic; }
</style>
</head>
<body>
<main class="poster">
  <div class="poster__photo" role="img" aria-label="Portrait of the artist wearing a pearl and wire crown against a misty wintry forest"></div>

  <p class="quote quote--left">“Rich and<br>expressive”<span class="quote__source">BdM Magazine</span></p>
  <p class="quote quote--right">“Vibrant and<br>experimental”<span class="quote__source">Tunepaths</span></p>

  <svg class="frame" width="667" height="942" viewBox="0 0 667 942" aria-hidden="true">
    <path d="M68 492 H29 V881 H638 V492 H599" fill="none" stroke="var(--frame-line)" stroke-width="1.5"/>
    <path d="M33 496 H29 M638 496 H634" stroke="var(--frame-line)" stroke-width="1"/>
  </svg>

  <h1 class="artist-name">Clara Joy Halden</h1>
  <p class="album-title">Lantern Waltz</p>
  <h2 class="tour-heading">Autumn / Winter Tour</h2>

  <ul class="dates">
    <li><span class="date">3<sup>RD</sup> September</span> <span class="city">Ravensby Folk Festival</span></li>
    <li><span class="date">21<sup>ST</sup> September</span> <span class="city">Swindon</span> <span class="venue">Calder Theatre</span></li>
    <li><span class="date">1<sup>ST</sup> October</span> <span class="city">Hitchin</span> <span class="venue">Brackwell Folk Club</span></li>
    <li><span class="date">17<sup>TH</sup> October</span> <span class="city">Bath</span> <span class="venue">The Anvil</span></li>
    <li><span class="date">20<sup>TH</sup> October</span> <span class="city">Sheffield</span> <span class="venue">Upper Dale Croquet Club</span></li>
    <li><span class="date">24<sup>TH</sup> October</span> <span class="city">Birmingham</span> <span class="venue">Orchard Lamp Cafe</span></li>
    <li><span class="date">26<sup>TH</sup> October</span> <span class="city">Glasgow</span> <span class="venue">The Nook and Jar</span></li>
    <li><span class="date">27<sup>TH</sup> October</span> <span class="city">Edinburgh</span> <span class="venue">The Marble Parlour</span></li>
    <li><span class="date">8<sup>TH</sup> November</span> <span class="city">Capital Reel &amp; Ballad Festival</span> <span class="venue">The Crooked Heron</span></li>
    <li><span class="date">25<sup>TH</sup> November</span> <span class="city">Lewes</span> <span class="venue">Tandem Record Shop (Live In Store)</span></li>
    <li><span class="date">2<sup>ND</sup> December</span> <span class="city">Cambridge</span> <span class="venue">The Quayside</span></li>
    <li><span class="date">27<sup>TH</sup> January</span> <span class="city">Lincolnshire</span> <span class="venue">Fenmarsh Theatre</span></li>
  </ul>

  <p class="tickets"><span class="tickets__label">Tickets/Info:</span> <span class="tickets__url">www.clarajoyhalden-music.example/gigs</span></p>
</main>
</body>
</html>
```